Website design for an events management company

What we need is the design of a website to be used by an events management company, the company is called "Vanto Events Management" and the website is expected to contain the following sections:
1) Homepage
2) Who are we?
3) Mission / Vision / Core values
4) Why to choose Vanto?
5) Past experience
6) Duties or provided services (Scientific Program Duties, Accreditation, Fund Raising, Accommodations, Social Activities, Transportation, Marketing of the Event, Publications and printed materials, Secretarial Work and Media Coverage)
7) References
8) Contact Us page (will probably contain a contact us form plus email, address and a google map)

Attached for your reference the company's logo

Expected that the winner should deliver the designs of at least two pages (the homepage plus an inner page) plus of course all the used graphics, images ... etc.

Thanks

Target Market(s)

The design need to target scientific events and not public events, for example the company doesn't organize music concerts ... etc., it organizes only scientific events so please target business users (i.e. doctors, engineers, scientisits ... etc) while making the designs, including the correct colors, images and icons

Industry/Entity Type

It Company

Number of Pages Required

2 page

Requirements
Must have
• One homepage
• One inner page
• All the used graphics and images
Nice to have
• More than two pages

```html
<!DOCTYPE html>
<html lang="en">
<head>
<meta charset="utf-8">
<title>Vanto Events Management</title>
<link rel="stylesheet" href="https://fonts.googleapis.com/css2?family=Didact+Gothic&family=Open+Sans:wght@400;600;700;800&display=swap">
<style>
:root{
  --ink:#111;
  --muted:#5a5a5a;
  --topbar:#c9c9cb;
  --white:#fff;
  --panel:#dcdde0;
  --hero-light:#8fb8e3;
  --hero-deep:#1d3566;
  --mint:#42e3a4;
  --teal:#2fa08e;
  --black:#000;
  --footer:#c6c6c8;
  --btn-border:#6a6a6a;
}
*{box-sizing:border-box;margin:0;padding:0}
html,body{width:758px;height:1200px;overflow:hidden}
body{
  position:relative;
  font-family:"Open Sans",Arial,sans-serif;
  color:var(--ink);
  background:radial-gradient(ellipse 62% 48% at 50% 46%,#ffffff 0%,#ececec 35%,#7a7a7a 72%,#1b1b1b 100%);
}
.abs{position:absolute}
/* top bar */
.topbar{left:0;top:0;width:758px;height:21px;background:var(--topbar)}
.topbar .item{position:absolute;top:4px;display:flex;align-items:center;gap:4px;font-size:8px;color:#333;font-weight:600}
.topbar .phone{left:150px}
.topbar .contact{left:224px}
.social{position:absolute;left:570px;top:5px;display:flex;gap:4px}
.social span{width:11px;height:11px;border-radius:50%;background:#111;display:block}
/* header */
.header{left:57px;top:21px;width:639px;height:63px;background:var(--white)}
.brand{position:absolute;left:86px;top:8px;width:96px;text-align:center}
.brand .mark{display:inline-flex;align-items:center;gap:5px;font-family:"Didact Gothic",sans-serif;font-size:22px;color:#6b6b6b;line-height:26px}
.brand .mark i{width:10px;height:10px;border-radius:50%;background:#9b7ec8;display:block}
.brand .full{font-size:8px;font-weight:700;color:var(--ink);white-space:nowrap;margin-top:4px}
.nav{position:absolute;left:249px;top:23px;display:flex}
.nav li{list-style:none;padding:0 7px 0 4px;border-left:1px solid #999;height:32px}
.nav li:first-child{border-left:none}
.nav b{display:block;font-size:7px;font-weight:700;color:#333;white-space:nowrap}
.nav small{display:block;font-size:5.5px;line-height:6px;font-weight:700;color:var(--ink);margin-top:3px;width:40px}
/* hero */
.hero{left:57px;top:84px;width:639px;height:240px;background:linear-gradient(90deg,#6e9fd4 0%,var(--hero-light) 60%,#b7d1ec 100%);overflow:hidden}
.hero-photo{position:absolute;left:0;top:0;width:342px;height:240px;background:linear-gradient(120deg,#0b1d45 0%,var(--hero-deep) 35%,#4f7fbf 70%,rgba(143,184,227,0) 100%)}
.hero-title{position:absolute;left:351px;top:33px;font-family:"Didact Gothic",sans-serif;font-size:19px;color:var(--white);letter-spacing:.3px}
.hero-rule{position:absolute;left:342px;top:61px;width:252px;height:1px;background:rgba(255,255,255,.8)}
.hero-text{position:absolute;left:351px;top:67px;width:152px;font-size:7px;line-height:8.4px;font-weight:700;color:var(--white)}
.hero-btn{position:absolute;left:351px;top:125px;width:69px;height:17px;border:1px solid var(--white);color:var(--white);font-size:5.5px;font-weight:800;display:flex;align-items:center;justify-content:center}
.swatches{position:absolute;left:355px;top:160px;display:flex;gap:11px}
.swatch{width:47px;text-align:center}
.swatch i{display:block;width:47px;height:47px;border-radius:50%}
.swatch span{display:block;font-size:7px;font-weight:700;color:#2d3f5e;margin-top:7px;white-space:nowrap}
.next{position:absolute;left:616px;top:91px;width:46px;height:47px;border-radius:50%;background:#dfe3e8}
/* services */
.panel{left:57px;top:324px;width:639px;height:820px;background:radial-gradient(ellipse 70% 55% at 50% 40%,#f6f6f6 0%,#e6e7e9 55%,var(--panel) 100%)}
.services{position:absolute;left:105px;top:344px;display:grid;grid-template-columns:repeat(3,185px);grid-auto-rows:215px}
.service{text-align:center}
.service .photo{display:block;width:100px;height:100px;border-radius:50%;margin:0 auto}
.service h3{font-size:10px;font-weight:700;color:var(--muted);margin-top:9px}
.service p{font-size:7px;line-height:8.6px;font-weight:700;color:var(--ink);width:110px;margin:4px auto 0}
.learn{display:inline-flex;align-items:center;justify-content:center;width:71px;height:17px;border:1px solid var(--btn-border);background:var(--white);font-size:5.5px;font-weight:800;color:#333;margin-top:5px}
/* newsletter */
.newsletter{left:147px;top:1017px;width:476px;height:127px;background:var(--black);border-radius:7px 7px 0 0;text-align:center;color:var(--white)}
.newsletter svg{margin-top:11px}
.newsletter h2{font-family:"Didact Gothic",sans-serif;font-weight:400;font-size:16px;margin-top:6px}
.newsletter .lead{font-size:10px;font-weight:700;margin-top:4px;margin-left:-56px}
.signup{position:absolute;left:143px;top:84px;display:flex;gap:5px}
.signup .field{width:153px;height:26px;background:var(--white);border-radius:6px;color:var(--ink);font-size:10px;font-weight:800;text-align:left;padding:6px 0 0 9px}
.signup .go{width:32px;height:32px;margin-top:-3px;background:#bdbdbd;border-radius:5px;display:flex;align-items:center;justify-content:center}
/* footer */
.footer{left:57px;top:1144px;width:639px;height:56px;background:var(--footer);text-align:center;font-size:7px;font-weight:700;color:var(--ink);padding-top:13px;line-height:10px}
</style>
</head>
<body>
<div class="abs topbar">
  <div class="item phone">
    <svg width="8" height="13" viewBox="0 0 8 13"><rect x="0.5" y="0.5" width="7" height="12" rx="1.5" fill="#111"/><rect x="1.5" y="2" width="5" height="8" fill="#c9c9cb"/></svg>
    000.000.1111
  </div>
  <div class="item contact">
    <svg width="13" height="9" viewBox="0 0 13 9"><rect width="13" height="9" fill="#111"/><path d="M0.5 0.5 L6.5 5 L12.5 0.5" stroke="#c9c9cb" fill="none"/></svg>
    Contact
  </div>
  <div class="social" aria-label="Social links"><span></span><span></span><span></span></div>
</div>

<header class="abs header">
  <div class="brand">
    <div class="mark"><i></i>Vanto</div>
    <div class="full">Vanto Events Management</div>
  </div>
  <ul class="nav">
    <li><b>Who are we?</b><small>Lorem ipsum dolor sit amet</small></li>
    <li><b>Mission</b><small>Lorem ipsum dolor sit amet</small></li>
    <li><b>Why to choose Vanto?</b><small>Lorem ipsum dolor sit amet</small></li>
    <li><b>Past experience</b><small>Lorem ipsum dolor sit amet</small></li>
    <li><b>References</b><small>Lorem ipsum dolor sit amet</small></li>
  </ul>
</header>

<section class="abs hero">
  <div class="hero-photo" role="img" aria-label="Glass office tower seen from below against a blue sky"></div>
  <h1 class="hero-title">SCIENTIFIC PROGRAM DUTIES</h1>
  <div class="hero-rule"></div>
  <p class="hero-text">Lorem ipsum dolor sit amet, consectetur adipisci elit, sed eiusmod tempor incidunt ut labore et dolore magna aliqua. Ut enim ad minim veniam, quis nostrum exercitationem ullam corporis suscipit laboriosam, nisi ut aliquid ex ea commodi consequatur.</p>
  <div class="hero-btn">LEARN MORE &gt;</div>
  <div class="swatches">
    <div class="swatch"><i style="background:var(--mint)"></i><span>Lorem ipsum</span></div>
    <div class="swatch"><i style="background:var(--teal)"></i><span>Lorem ipsum</span></div>
    <div class="swatch"><i style="background:var(--black)"></i><span>Lorem ipsum</span></div>
  </div>
  <div class="next">
    <svg width="46" height="47" viewBox="0 0 46 47"><path d="M11 19 L18 23.5 L11 28 Z" fill="#8a8f96"/></svg>
  </div>
</section>

<main class="abs panel"></main>
<div class="services">
  <article class="service">
    <span class="photo" role="img" aria-label="Speaker presenting to a seated audience in a conference hall" style="background:radial-gradient(circle at 50% 35%,#9cc3e6,#2c5a8c 60%,#0d1f36)"></span>
    <h3>Scientific Program Duties</h3>
    <p>Lorem ipsum dolor sit amet, consectetur adipisci elit, sed eiusmod tempor incidunt ut labore et dolore magna aliqua.</p>
    <span class="learn">LEARN MORE &gt;</span>
  </article>
  <article class="service">
    <span class="photo" role="img" aria-label="Business people talking at an evening networking event" style="background:radial-gradient(circle at 40% 30%,#c07a4a,#2a3350 55%,#0f1428)"></span>
    <h3>Accreditation</h3>
    <p>Lorem ipsum dolor sit amet, consectetur adipisci elit, sed eiusmod tempor incidunt ut labore et dolore magna aliqua.</p>
    <span class="learn">LEARN MORE &gt;</span>
  </article>
  <article class="service">
    <span class="photo" role="img" aria-label="Professionals seated in a bright meeting room" style="background:radial-gradient(circle at 50% 40%,#f1ece4,#b9a892 60%,#4a4038)"></span>
    <h3>Fund Raising</h3>
    <p>Lorem ipsum dolor sit amet, consectetur adipisci elit, sed eiusmod tempor incidunt ut labore et dolore magna aliqua.</p>
    <span class="learn">LEARN MORE &gt;</span>
  </article>
  <article class="service">
    <span class="photo" role="img" aria-label="Laptop screen showing colourful bar charts" style="background:radial-gradient(circle at 50% 50%,#d9e6f2,#6f8fb0 55%,#2a2a2a)"></span>
    <h3>Accommodations</h3>
    <p>Lorem ipsum dolor sit amet, consectetur adipisci elit, sed eiusmod tempor incidunt ut labore et dolore magna aliqua.</p>
    <span class="learn">LEARN MORE &gt;</span>
  </article>
  <article class="service">
    <span class="photo" role="img" aria-label="Scientist working with equipment in a laboratory" style="background:radial-gradient(circle at 50% 45%,#eef3f6,#a9c1d0 55%,#4f6a7c)"></span>
    <h3>Social activities</h3>
    <p>Lorem ipsum dolor sit amet, consectetur adipisci elit, sed eiusmod tempor incidunt ut labore et dolore magna aliqua.</p>
    <span class="learn">LEARN MORE &gt;</span>
  </article>
  <article class="service">
    <span class="photo" role="img" aria-label="Car interior on a road at dusk" style="background:radial-gradient(circle at 50% 35%,#e5b98a,#6b4a5c 50%,#1a1420)"></span>
    <h3>Transportation</h3>
    <p>Lorem ipsum dolor sit amet, consectetur adipisci elit, sed eiusmod tempor incidunt ut labore et dolore magna aliqua.</p>
    <span class="learn">LEARN MORE &gt;</span>
  </article>
  <article class="service">
    <span class="photo" role="img" aria-label="Hands typing on a computer keyboard" style="background:radial-gradient(circle at 50% 50%,#e6e6e6,#8e9296 55%,#2d3034)"></span>
    <h3>Lorem ipsum</h3>
    <p>Lorem ipsum dolor sit amet, consectetur adipisci elit, sed eiusmod tempor incidunt ut labore et dolore magna aliqua.</p>
    <span class="learn">LEARN MORE &gt;</span>
  </article>
  <article class="service">
    <span class="photo" role="img" aria-label="Hand signing a printed document with a pen" style="background:radial-gradient(circle at 50% 50%,#fafafa,#c8c8c8 55%,#3a3a3a)"></span>
    <h3>Lorem ipsum</h3>
    <p>Lorem ipsum dolor sit amet, consectetur adipisci elit, sed eiusmod tempor incidunt ut labore et dolore magna aliqua.</p>
    <span class="learn">LEARN MORE &gt;</span>
  </article>
  <article class="service">
    <span class="photo" role="img" aria-label="Desk with laptop, notes and coffee seen from above" style="background:radial-gradient(circle at 50% 50%,#d8cbb6,#8c7458 55%,#3c3026)"></span>
    <h3>Lorem ipsum</h3>
    <p>Lorem ipsum dolor sit amet, consectetur adipisci elit, sed eiusmod tempor incidunt ut labore et dolore magna aliqua.</p>
    <span class="learn">LEARN MORE &gt;</span>
  </article>
</div>

<section class="abs newsletter">
  <svg width="32" height="23" viewBox="0 0 32 23"><rect x="1" y="1" width="30" height="21" fill="none" stroke="#fff" stroke-width="2"/><path d="M1 1 L16 13 L31 1" fill="none" stroke="#fff" stroke-width="2"/><path d="M1 22 L12 10 M31 22 L20 10" stroke="#fff" stroke-width="1.5"/></svg>
  <h2>SUBSCRIBE TO THE NEWSLETTER</h2>
  <p class="lead">Read about the latest news</p>
  <div class="signup">
    <div class="field">your email</div>
    <div class="go"><svg width="20" height="16" viewBox="0 0 20 16"><path d="M2 8 L8 14 L18 2" fill="none" stroke="#111" stroke-width="3.5"/></svg></div>
  </div>
</section>

<footer class="abs footer">
  Home| Who are we?| Mission / Vision / Core values| Why to choose Vanto?| Past experience| References| Contact<br>
  ©2015 Copyright VANTO Events Management. All Rights Reservede.
</footer>
</body>
</html>
```